New cookbook recipes app with New Technology Devices

App description:
Main features description that differentiates it from the current apps on the market:
Beautiful recipe cookbook app -> great look&feel and great UX;
Mise en Place Tab (Sort/Setup) -> Instead to have only the ingredients and the steps to cook Tab this new/different tab will help the cook to get all ingredients(raw or pre-cooked) organized and in order to be used on the recipe. This is a game changer in the cook learn-process.
Will change/present/show a different concept for measure/count quantities. Instead of display only the cups/pinch/time-to-cook/table-spoon etc (non-precision units), will have all these units converted in grams/pounds and cook internal temperatures.

Other features:
The app will work in all devices (phones, tablets, and desktops);
Good search tool by category or term filtration system;
No ads on the app (will be a subscription fee monetization method);
Inside the recipe the app will show the quantities in the usual way (spoons, pinches, and others) and new way (grams or lb);
Serving change capability (e.g. Serving for 2 persons can change to 4 people and the app will calculate the ingredients for that);
Pixolune and social media share capability;
If the user is logged in, the favorites will be enabled (user can save their fav recipes);
The app will allow recording videos and photos of the making process to share on social media.

Result expected:
I need a non-workable app, showing the app Design and Flow, to work on Tablets and Phones.

Target Market(s)

Cooks, average people looking for new technologies to cook

Font styles to use
Serif
Sans Serif

Requirements
Must have
• Great look and feel.
Serving change capability and unit conversion
Should not have
• Ads on the app

```html
<!DOCTYPE html>
<html lang="en">
<head>
<meta charset="UTF-8">
<title>Ingredient Settings</title>
<link rel="stylesheet" href="https://fonts.googleapis.com/css2?family=Poppins:wght@400;600;700&display=swap">
<style>
  :root {
    --brand-red: #b93c48;
    --cream: #fde1d8;
    --ink: #2b2b2b;
    --field-border: #e6e6e6;
    --white: #ffffff;
    --pattern-tint: rgba(185, 60, 72, 0.10);
  }
  * { box-sizing: border-box; margin: 0; padding: 0; }
  html, body { width: 768px; height: 1200px; overflow: hidden; }
  body {
    font-family: "Poppins", sans-serif;
    background: var(--white);
    position: relative;
  }
  .app-header {
    position: absolute; top: 0; left: 0; width: 768px; height: 180px;
    background: var(--brand-red);
  }
  .back-button {
    position: absolute; left: 22px; top: 118px; width: 28px; height: 28px;
  }
  .screen-title {
    position: absolute; top: 108px; left: 0; width: 768px;
    text-align: center; color: var(--cream);
    font-weight: 700; font-size: 33px; line-height: 48px; letter-spacing: 0.3px;
  }
  .content-backdrop {
    position: absolute; top: 180px; left: 0; width: 768px; height: 900px;
    background-color: var(--white);
    background-image:
      radial-gradient(circle at 216px 72px, var(--pattern-tint) 0, transparent 62px),
      radial-gradient(circle at 576px 24px, var(--pattern-tint) 0, transparent 58px),
      radial-gradient(circle at 114px 240px, var(--pattern-tint) 0, transparent 60px),
      radial-gradient(circle at 730px 216px, var(--pattern-tint) 0, transparent 60px),
      radial-gradient(circle at 546px 336px, var(--pattern-tint) 0, transparent 58px),
      radial-gradient(circle at 274px 408px, var(--pattern-tint) 0, transparent 58px),
      radial-gradient(circle at 740px 444px, var(--pattern-tint) 0, transparent 56px),
      radial-gradient(circle at 48px 552px, var(--pattern-tint) 0, transparent 64px),
      radial-gradient(circle at 446px 544px, var(--pattern-tint) 0, transparent 66px),
      radial-gradient(circle at 720px 708px, var(--pattern-tint) 0, transparent 62px),
      radial-gradient(circle at 108px 780px, var(--pattern-tint) 0, transparent 62px),
      radial-gradient(circle at 502px 774px, var(--pattern-tint) 0, transparent 62px),
      radial-gradient(circle at 314px 860px, var(--pattern-tint) 0, transparent 56px);
  }
  .settings-section { position: absolute; top: 233px; left: 25px; width: 700px; }
  .section-title { font-weight: 600; font-size: 20px; color: var(--ink); line-height: 30px; }
  .field-label {
    margin: 23px 0 0 23px; font-size: 22px; color: var(--ink); line-height: 32px;
  }
  .select-field {
    margin: 8px 0 0 19px; width: 681px; height: 62px;
    background: var(--white); border: 2px solid var(--field-border);
    border-radius: 12px; box-shadow: 0 2px 4px rgba(0,0,0,0.06);
    display: flex; align-items: center; justify-content: space-between;
    padding: 0 22px 0 24px; font-size: 19px; color: var(--ink);
  }
  .field-group + .field-group .field-label { margin-top: 28px; }
  .bottom-nav {
    position: absolute; left: 0; top: 1080px; width: 768px; height: 120px;
    background: var(--brand-red);
  }
  .nav-icon { position: absolute; top: 36px; width: 48px; height: 48px; }
</style>
</head>
<body>
  <header class="app-header">
    <svg class="back-button" viewBox="0 0 28 28" aria-label="Back">
      <path d="M17 6 L9 14 L17 22" fill="none" stroke="var(--cream)" stroke-width="3.5" stroke-linecap="round" stroke-linejoin="round"/>
    </svg>
    <h1 class="screen-title">INGREDIENT SETTINGS</h1>
  </header>

  <div class="content-backdrop" role="img" aria-label="Faint pattern of food outline icons: sushi, burger, skewers, toast, donut, pancakes, pizza slice, fries, chocolate bar, hot dog"></div>

  <main class="settings-section">
    <h2 class="section-title">Measurement Conversion</h2>
    <div class="field-group">
      <p class="field-label">Weight</p>
      <div class="select-field">
        <span>Grams</span>
        <svg width="20" height="14" viewBox="0 0 20 14"><path d="M3 3 L10 10 L17 3" fill="none" stroke="var(--ink)" stroke-width="3.5" stroke-linecap="round" stroke-linejoin="round"/></svg>
      </div>
    </div>
    <div class="field-group">
      <p class="field-label">Weight</p>
      <div class="select-field">
        <span>Cups</span>
        <svg width="20" height="14" viewBox="0 0 20 14"><path d="M3 3 L10 10 L17 3" fill="none" stroke="var(--ink)" stroke-width="3.5" stroke-linecap="round" stroke-linejoin="round"/></svg>
      </div>
    </div>
  </main>

  <nav class="bottom-nav">
    <svg class="nav-icon" style="left:101px" viewBox="0 0 48 48" aria-label="Home">
      <path d="M24 5 L3 24 H9 V44 H19 V32 H29 V44 H39 V24 H45 Z" fill="var(--cream)"/>
    </svg>
    <svg class="nav-icon" style="left:228px" viewBox="0 0 48 48" aria-label="Messages">
      <rect x="4" y="10" width="40" height="29" rx="3" fill="var(--cream)"/>
      <path d="M4 13 L24 27 L44 13" fill="none" stroke="var(--brand-red)" stroke-width="3"/>
    </svg>
    <svg class="nav-icon" style="left:358px" viewBox="0 0 48 48" aria-label="Add recipe">
      <circle cx="24" cy="24" r="22" fill="var(--cream)"/>
      <path d="M24 13 V35 M13 24 H35" stroke="var(--brand-red)" stroke-width="4" stroke-linecap="round"/>
    </svg>
    <svg class="nav-icon" style="left:489px" viewBox="0 0 48 48" aria-label="Favorites">
      <path d="M24 44 L6 26 C-1 19 3 6 13 6 C18 6 22 9 24 13 C26 9 30 6 35 6 C45 6 49 19 42 26 Z" fill="var(--cream)"/>
    </svg>
    <svg class="nav-icon" style="left:622px" viewBox="0 0 48 48" aria-label="Profile">
      <circle cx="24" cy="24" r="23" fill="var(--cream)"/>
      <circle cx="24" cy="18" r="8" fill="var(--brand-red)"/>
      <path d="M10 38 C13 30 35 30 38 38 C34 43 14 43 10 38 Z" fill="var(--brand-red)"/>
    </svg>
  </nav>
</body>
</html>
```